Quillmont Booking Engine Marketing Site

Hi,
I’m currently in the process of putting together a web application with the intention of providing small resorts/B&Bs/small hotels the ability to allow their customers to book online.
I’m looking to have a design created for a marketing site, to give potential customers additional information about my booking engine, as well as to help drive sign-ups. A lot of the competition out there appears outdated, so I would like something that is more modern and up to date.
I am looking for just the design (i’m a web developer, but I lack the creative skills for a good marketing site)
For some more background, I will be targeting business owners of smaller resorts and Bed & Breakfasts. These are typically family owned small businesses that may only have a 10 room setup. These businesses will also typically have additional amenities that they will have to rent out or sell to their clients ( ex. Spa, fruit basket, water sport rentals). My software will provide them with the ability to sell their amenities as well.
I’m open to different designs, but my main thing is I want it to look modern, and I want it to have several callouts to sign up for my product.
I am looking to have the homepage created, 1 interior page, and a style guide created (to show form fields, H1’s, etc.).
I had a logo created a couple months ago that will be included with this project brief.
If you need any additional information feel free to reach out to me.

Target Market(s)

This site will be targeted small business owners who are running small resorts, Bed and Breakfasts, or any business that provides rooms for their clients.

Industry/Entity Type

Saas

Number of Pages Required

2 page

Font styles to use
Sans Serif

Colors

Designer to choose colors to be used in the design.

Requirements
Must have
• A modern feel, with several CTA's that will drive to the registration page on the homepage. on the internal page, I mostly just need the page layout, I will reuse that page layout. and a style guide if at all possible (include colors, form fields, H1's, etc.)
Nice to have
• maybe a hero image at the top with buttons over the top? again i'm pretty open to most anything.
Should not have
• I like images, but I don't want the page overrun with images. A good balance.

```html
<!DOCTYPE html>
<html lang="en">
<head>
<meta charset="utf-8">
<title>Quillmont Booking Engine</title>
<link href="https://fonts.googleapis.com/css2?family=Roboto:wght@400;500;700&family=Roboto+Condensed:wght@400;700&display=swap" rel="stylesheet">
<style>
:root{
  --navy:#1d4b7a;
  --nav-blue:#1a64a8;
  --green:#5ea51e;
  --green-dark:#3f7d0e;
  --text:#555;
  --dark:#333;
  --light:#e7eef5;
  --teal:#17707f;
  --orange:#e6531c;
  --footer:#f2f2f2;
  --band:#0d3f78;
}
*{margin:0;padding:0;box-sizing:border-box}
html,body{width:1200px;height:4712px;overflow:hidden}
body{font-family:"Roboto",Arial,sans-serif;color:var(--text);background:#fff;position:relative}
.section{position:absolute;left:0;width:1200px;overflow:hidden}
.abs{position:absolute}
.btn{position:absolute;display:flex;align-items:center;justify-content:center;border-radius:30px;color:#fff;font-family:"Roboto Condensed",Arial,sans-serif;font-weight:700;font-size:17px;text-transform:uppercase;background:linear-gradient(#7cc02c,var(--green-dark));box-shadow:0 3px 6px rgba(0,0,0,.25)}
.h2{font-family:"Roboto Condensed",Arial,sans-serif;font-weight:400;color:var(--navy);text-transform:uppercase;font-size:34px;line-height:1.15}
p{font-size:14.5px;line-height:1.7}
.placeholder{position:absolute}

/* nav */
.nav{top:0;height:70px;background:#fff}
.logo{position:absolute;left:70px;top:12px;display:flex;align-items:center;gap:8px}
.logo-dot{width:40px;height:40px;border-radius:50%;background:var(--green)}
.logo-name{font-family:"Roboto",sans-serif;font-weight:700;color:var(--nav-blue);font-size:19px;line-height:1.05;text-transform:uppercase}
.logo-name small{display:block;font-size:13px;font-weight:700}
.menu{position:absolute;left:306px;top:27px;display:flex;gap:27px;font-size:13px;font-weight:500;color:#444;text-transform:uppercase}
.sign-in{position:absolute;left:889px;top:17px;width:94px;height:38px;background:var(--nav-blue);color:#fff;font-size:13px;font-weight:500;display:flex;align-items:center;justify-content:center;text-transform:uppercase}
.sign-up{position:absolute;left:993px;top:17px;width:132px;height:38px;background:var(--green);color:#fff;font-size:13px;font-weight:500;display:flex;align-items:center;justify-content:center;text-transform:uppercase}

/* hero */
.hero{top:70px;height:659px}
.hero-photo{left:0;top:0;width:1200px;height:659px;background:linear-gradient(180deg,#8fb7c7 0%,#b9ccc9 35%,#c9b89c 70%,#8c7a63 100%)}
.hero-title{left:75px;top:165px;width:330px;color:#fff;font-family:"Roboto Condensed",sans-serif;font-weight:700;font-size:29px;line-height:1.2;text-transform:uppercase;text-shadow:0 1px 3px rgba(0,0,0,.3)}
.hero-screen{left:597px;top:133px;width:500px;height:320px;background:linear-gradient(#f4f6f8,#dfe4e9);border:14px solid #1e1e1e;border-radius:8px}
.hero-lens{left:420px;top:84px;width:240px;height:240px;border-radius:50%;background:#fff;border:10px solid #222}

/* features */
.features{top:729px;height:848px;background:linear-gradient(#eaf1f7,#f6f9fb)}
.features .h2{position:absolute;top:78px;width:1200px;text-align:center}
.features .intro{position:absolute;left:150px;top:125px;width:900px;text-align:center;font-size:14px}
.tablet{left:432px;top:336px;width:336px;height:316px;background:linear-gradient(135deg,#2b2b2b,#4a4a4a);border-radius:18px;box-shadow:0 10px 24px rgba(0,0,0,.25)}
.feat{position:absolute;width:130px;text-align:center;font-size:14px;color:var(--dark);line-height:1.25}
.feat svg{display:block;margin:0 auto 8px;width:40px;height:40px}

/* simple */
.simple{top:1577px;height:591px;background:#fff}
.simple .h2{position:absolute;left:69px;top:60px;width:470px}
.simple p{position:absolute;left:69px;top:215px;width:450px}
.shot{left:567px;top:94px;width:633px;height:402px;background:linear-gradient(#f5f7f9,#e3e8ec);border:1px solid #d5dbe0;box-shadow:0 6px 18px rgba(0,0,0,.15)}

/* workflow */
.workflow{top:2168px;height:653px;background:linear-gradient(120deg,#dde7f0 0%,#eef3f8 50%,#e3ebf3 100%)}
.workflow .band{position:absolute;left:0;top:565px;width:1200px;height:88px;background:var(--band)}
.imac{left:63px;top:69px;width:487px;height:584px;background:linear-gradient(#d9dde1,#bfc5cb)}
.workflow .h2{position:absolute;left:609px;top:69px;width:560px}
.checks{position:absolute;left:609px;top:130px;list-style:none}
.checks li{font-size:14.5px;height:40px;display:flex;align-items:center;gap:10px}
.checks svg{width:18px;height:18px;flex:none}

/* testimonials */
.testimonials{top:2821px;height:682px;background:#fff}
.testimonials .h2{position:absolute;top:80px;width:1200px;text-align:center}
.card{position:absolute;top:212px;width:332px;text-align:center}
.card .q{width:34px;height:34px;border-radius:50%;background:var(--navy);margin:0 auto 14px;display:flex;align-items:center;justify-content:center;color:#fff;font-size:26px;font-family:Georgia,serif;line-height:1}
.card p{font-size:14.5px;color:#444;line-height:1.6}
.avatar{width:50px;height:50px;border-radius:50%;background:#b8c2cc;margin:28px auto 8px}
.card .name{font-size:20px;color:var(--navy);font-family:"Roboto Condensed",sans-serif}
.card .role{font-size:13px;color:#777}
.divider{position:absolute;top:212px;width:1px;height:280px;background:#ddd}
.dots{position:absolute;top:588px;left:0;width:1200px;display:flex;justify-content:center;gap:6px}
.dots i{width:14px;height:14px;border-radius:50%;border:1.5px solid var(--navy)}
.dots i:first-child{background:var(--navy)}

/* success */
.success{top:3503px;height:631px;background:linear-gradient(90deg,#1a6172,#1d7c8c 55%,#2c8c99)}
.success .h2{position:absolute;top:68px;width:1200px;text-align:center;color:#fff}
.success p{position:absolute;color:#fff;width:1200px;text-align:center}
.success svg{position:absolute}

/* cta */
.cta{top:4134px;height:154px;background:linear-gradient(90deg,#d9481a,#ee6a1e)}
.cta h3{position:absolute;left:69px;top:38px;color:#fff;font-size:32px;font-weight:700}
.cta .sub{position:absolute;left:69px;top:86px;color:#fff;font-size:19px}

/* footer */
.footer{top:4288px;height:424px;background:var(--footer)}
.footer h4{position:absolute;font-size:14px;color:var(--dark);font-weight:700}
.footer .col{position:absolute;font-size:13px;line-height:1.75;color:#555}
.social{position:absolute;left:883px;top:84px;display:flex;gap:10px}
.social i{width:38px;height:38px;border-radius:50%;border:2px solid #555}
.phone{position:absolute;left:883px;font-size:30px;color:var(--dark)}
.copy{position:absolute;left:69px;top:374px;font-size:12px;color:#666}
</style>
</head>
<body>

<header class="section nav">
  <div class="logo"><span class="logo-dot"></span><span class="logo-name">Quillmont<small>Booking Engine</small></span></div>
  <nav class="menu"><span>Home</span><span>Features</span><span>About Us</span><span>Support</span><span>Testimonials</span><span>Contact Us</span></nav>
  <span class="sign-in">Sign In</span>
  <span class="sign-up">Free Sign Up</span>
</header>

<section class="section hero">
  <div class="placeholder hero-photo" role="img" aria-label="Photo of a bright resort terrace overlooking the sea"></div>
  <h1 class="abs hero-title">We providing small resorts/B&amp;Bs/small hotels the ability to allow their customers to book online.</h1>
  <div class="placeholder hero-screen" role="img" aria-label="Laptop showing the booking calendar screen"></div>
  <div class="placeholder hero-lens" role="img" aria-label="Magnified view of the reservations menu"></div>
  <span class="btn" style="left:75px;top:426px;width:265px;height:46px">Start Your Free Trial</span>
</section>

<section class="section features">
  <h2 class="h2">A Powerful and Innovative Features Set</h2>
  <p class="intro">Lorem ipsum dolor sit amet, consectetur adipiscing elit, sed do eiusmod tempor incididunt ut labore et dolore magna aliqua. Ut enim ad minim veniam, quis nostrud exercitation ullamco laboris nisi ut aliquip ex ea commodo consequat.</p>
  <div class="placeholder tablet" role="img" aria-label="Tablet showing the room management screen"></div>

  <div class="feat" style="left:447px;top:205px"><svg viewBox="0 0 40 40" fill="none" stroke="#1d4b7a" stroke-width="2"><path d="M6 34V14l14-8 14 8v20z"/><rect x="15" y="22" width="10" height="12"/></svg>Property<br>Management</div>
  <div class="feat" style="left:623px;top:205px"><svg viewBox="0 0 40 40" fill="none" stroke="#1d4b7a" stroke-width="2"><rect x="6" y="8" width="28" height="20" rx="2"/><path d="M14 34h12M20 28v6"/></svg>Online<br>Booking</div>
  <div class="feat" style="left:783px;top:252px"><svg viewBox="0 0 40 40" fill="none" stroke="#1d4b7a" stroke-width="2"><rect x="9" y="5" width="22" height="30"/><path d="M14 13h12M14 19h12M14 25h8"/></svg>Invoicing</div>
  <div class="feat" style="left:280px;top:252px"><svg viewBox="0 0 40 40" fill="none" stroke="#1d4b7a" stroke-width="2"><path d="M5 30h30M8 30V18h24v12M12 18v-6h16v6"/></svg>Amenity<br>Management</div>
  <div class="feat" style="left:139px;top:352px"><svg viewBox="0 0 40 40" fill="none" stroke="#1d4b7a" stroke-width="2"><rect x="6" y="9" width="28" height="25" rx="2"/><path d="M6 16h28M13 5v7M27 5v7"/></svg>Booking<br>Management</div>
  <div class="feat" style="left:933px;top:352px"><svg viewBox="0 0 40 40" fill="none" stroke="#1d4b7a" stroke-width="2"><circle cx="20" cy="20" r="12"/><circle cx="20" cy="8" r="4"/><circle cx="8" cy="26" r="4"/><circle cx="32" cy="26" r="4"/></svg>Multi-User<br>Capabilities</div>
  <div class="feat" style="left:98px;top:509px"><svg viewBox="0 0 40 40" fill="none" stroke="#1d4b7a" stroke-width="2"><path d="M4 34V16l10-6 10 6v18M24 34V20l8-4 6 4v14"/></svg>Multi-Property<br>Capabilities</div>
  <div class="feat" style="left:933px;top:509px"><svg viewBox="0 0 40 40" fill="none" stroke="#1d4b7a" stroke-width="2"><circle cx="12" cy="12" r="5"/><circle cx="28" cy="28" r="5"/><path d="M30 8L10 32"/></svg>Promotions<br>Capabilities</div>
  <div class="feat" style="left:280px;top:616px"><svg viewBox="0 0 40 40" fill="none" stroke="#1d4b7a" stroke-width="2"><circle cx="20" cy="20" r="13"/><path d="M20 12v16M15 16h8a3 3 0 010 6h-6a3 3 0 000 6h8"/></svg>Rates<br>Management</div>
  <div class="feat" style="left:783px;top:616px"><svg viewBox="0 0 40 40" fill="none" stroke="#1d4b7a" stroke-width="2"><rect x="9" y="5" width="22" height="30"/><circle cx="25" cy="20" r="1.5"/></svg>Ability to<br>Add/Manage<br>Rooms/Units</div>
  <div class="feat" style="left:623px;top:668px"><svg viewBox="0 0 40 40" fill="none" stroke="#1d4b7a" stroke-width="2"><rect x="8" y="5" width="24" height="30"/><path d="M14 28v-6M20 28v-10M26 28v-4"/></svg>Reporting</div>
  <div class="feat" style="left:447px;top:676px"><svg viewBox="0 0 40 40" fill="none" stroke="#1d4b7a" stroke-width="2"><path d="M5 34h30M5 34V6M9 28l8-9 6 5 10-13"/></svg>Integrated<br>Analytics<br>Tracking</div>
</section>

<section class="section simple">
  <h2 class="h2">Simple, Powerful, Reliable Quillmont Booking Engine System</h2>
  <p>Lorem ipsum dolor sit amet, consectetur adipiscing elit, sed do eiusmod tempor incididunt ut labore et dolore magna aliqua. Ut enim ad minim veniam, quis nostrud exercitation ullamco laboris nisi ut aliquip ex ea commodo consequat. Duis aute irure dolor in reprehenderit in voluptate velit esse cillum dolore eu fugiat nulla pariatur. Excepteur sint occaecat cupidatat non proident, sunt in culpa qui officia deserunt mollit anim id est laborum.</p>
  <span class="btn" style="left:69px;top:465px;width:270px;height:46px">Start Your Free Trial</span>
  <div class="placeholder shot" role="img" aria-label="Browser window showing the reservations dashboard"></div>
</section>

<section class="section workflow">
  <div class="band"></div>
  <div class="placeholder imac" role="img" aria-label="Desktop computer displaying the booking workflow screen"></div>
  <h2 class="h2">Smart and Efficient Workfliw</h2>
  <ul class="checks">
    <li><svg viewBox="0 0 18 18"><circle cx="9" cy="9" r="8" fill="#1d4b7a"/><path d="M5 9l3 3 5-6" stroke="#fff" stroke-width="2" fill="none"/></svg>Lorem ipsum dolor sit amet, consectetur adipiscing elit.</li>
    <li><svg viewBox="0 0 18 18"><circle cx="9" cy="9" r="8" fill="#1d4b7a"/><path d="M5 9l3 3 5-6" stroke="#fff" stroke-width="2" fill="none"/></svg>Sed aliquet dolor in ullamcorper egestas.</li>
    <li><svg viewBox="0 0 18 18"><circle cx="9" cy="9" r="8" fill="#1d4b7a"/><path d="M5 9l3 3 5-6" stroke="#fff" stroke-width="2" fill="none"/></svg>In non augue fermentum, consequat lacus lobortis, vehicula ante.</li>
    <li><svg viewBox="0 0 18 18"><circle cx="9" cy="9" r="8" fill="#1d4b7a"/><path d="M5 9l3 3 5-6" stroke="#fff" stroke-width="2" fill="none"/></svg>Fusce a nibh in nisi scelerisque imperdiet auctor at eros.</li>
    <li><svg viewBox="0 0 18 18"><circle cx="9" cy="9" r="8" fill="#1d4b7a"/><path d="M5 9l3 3 5-6" stroke="#fff" stroke-width="2" fill="none"/></svg>Fusce lacinia massa eget dolor ullamcorper, vitae faucibus.</li>
    <li><svg viewBox="0 0 18 18"><circle cx="9" cy="9" r="8" fill="#1d4b7a"/><path d="M5 9l3 3 5-6" stroke="#fff" stroke-width="2" fill="none"/></svg>Etiam sollicitudin nisi eu interdum fermentum.</li>
    <li><svg viewBox="0 0 18 18"><circle cx="9" cy="9" r="8" fill="#1d4b7a"/><path d="M5 9l3 3 5-6" stroke="#fff" stroke-width="2" fill="none"/></svg>Sed a orci mattis, egestas augue ut, sodales sapien.</li>
    <li><svg viewBox="0 0 18 18"><circle cx="9" cy="9" r="8" fill="#1d4b7a"/><path d="M5 9l3 3 5-6" stroke="#fff" stroke-width="2" fill="none"/></svg>Etiam sollicitudin nisi eu interdum fermentum.</li>
  </ul>
  <span class="btn" style="left:622px;top:471px;width:258px;height:46px">Start Your Free Trial</span>
</section>

<section class="section testimonials">
  <h2 class="h2">Customer Say Something<br>- Testimonials</h2>
  <div class="card" style="left:69px"><div class="q">&ldquo;</div><p>&ldquo; Class aptent taciti sociosqu ad litora torquent per conubia nostra, per inceptos himenaeos. Mauris in erat justo. Nullam ac fermentum nunc. Etiam pharetra, erat sed fermentum feugiat, velit mauris egestas quam, ut aliquam massa nisl quis neque.&rdquo;</p><div class="avatar" role="img" aria-label="Customer portrait"></div><div class="name">Warren Dale</div><div class="role">Lorem ipsum dolor sit</div></div>
  <div class="divider" style="left:420px"></div>
  <div class="card" style="left:434px"><div class="q">&ldquo;</div><p>&ldquo; Class aptent taciti sociosqu ad litora torquent per conubia nostra, per inceptos himenaeos. Mauris in erat justo. Nullam ac fermentum nunc. Etiam pharetra, erat sed fermentum feugiat, velit mauris egestas quam, ut aliquam massa nisl quis neque.&rdquo;</p><div class="avatar" role="img" aria-label="Customer portrait"></div><div class="name">Warren Dale</div><div class="role">Lorem ipsum dolor sit</div></div>
  <div class="divider" style="left:783px"></div>
  <div class="card" style="left:798px"><div class="q">&ldquo;</div><p>&ldquo; Class aptent taciti sociosqu ad litora torquent per conubia nostra, per inceptos himenaeos. Mauris in erat justo. Nullam ac fermentum nunc. Etiam pharetra, erat sed fermentum feugiat, velit mauris egestas quam, ut aliquam massa nisl quis neque.&rdquo;</p><div class="avatar" role="img" aria-label="Customer portrait"></div><div class="name">Warren Dale</div><div class="role">Lorem ipsum dolor sit</div></div>
  <div class="dots"><i></i><i></i><i></i><i></i><i></i></div>
</section>

<section class="section success" role="img" aria-label="Teal-toned photo of a support agent wearing a headset">
  <h2 class="h2">Customer Success Team</h2>
  <p style="top:126px;left:0;padding:0 300px;font-size:15px">Lorem ipsum dolor sit amet, consectetur adipiscing elit, sed do eiusmod tempor incididunt ut labore et dolore magna aliqua.</p>
  <svg viewBox="0 0 80 80" style="left:560px;top:212px;width:80px;height:80px" fill="none" stroke="#fff" stroke-width="2.5"><rect x="10" y="40" width="60" height="30" rx="3"/><circle cx="40" cy="22" r="10"/><path d="M26 22a14 14 0 0128 0"/><text x="40" y="62" fill="#fff" stroke="none" font-size="16" text-anchor="middle" font-family="Roboto">7</text></svg>
  <p style="top:313px;font-size:15px">7 days a week support.</p>
  <svg viewBox="0 0 100 100" style="left:550px;top:375px;width:100px;height:100px" fill="none" stroke="#fff" stroke-width="2.5"><rect x="40" y="10" width="52" height="36"/><circle cx="24" cy="30" r="8"/><path d="M12 90V52h24v38M36 58l14-14"/><path d="M50 22h34M50 32h24"/></svg>
  <p style="top:500px;left:0;padding:0 330px;font-size:15px">Train your team and works with them for as long as needed for them to make the best use of Quillmont Booking Engine.</p>
</section>

<section class="section cta">
  <h3>Ready to get started?</h3>
  <div class="sub">Schedule a demo, and try Quillmont Booking Engine for free</div>
  <span class="btn" style="left:829px;top:44px;width:296px;height:63px;font-size:20px">Contact Us</span>
</section>

<footer class="section footer">
  <div class="logo" style="left:69px;top:30px"><span class="logo-dot"></span><span class="logo-name">Quillmont<small>Booking Engine</small></span></div>
  <h4 style="left:69px;top:118px">About Us</h4>
  <div class="col" style="left:69px;top:142px;width:290px">Lorem ipsum dolor sit amet, consectetur adipiscing elit, sed do eiusmod tempor incididunt ut labore et dolore magna aliqua. Ut enim ad minim veniam, quis nostrud exercitation ullamco laboris nisi ut aliquip ex ea commodo consequat. Duis aute irure.</div>
  <h4 style="left:399px;top:42px">Contact Us</h4>
  <div class="col" style="left:399px;top:68px;width:200px">Quillmont Booking Engine<br>220, lorem ipsum dolor sit,<br>dosis etrehet - 54856<br><br>E: hello@quillmontbooking.com</div>
  <h4 style="left:616px;top:42px">Quick Links</h4>
  <div class="col" style="left:616px;top:68px">Home<br>Features<br>About Us<br>Support<br>Testimonials<br>Contact Us</div>
  <h4 style="left:745px;top:42px">Info Links</h4>
  <div class="col" style="left:745px;top:68px">Terms of Use<br>Privacy Policy<br>Sitemap<br>Help!</div>
  <h4 style="left:883px;top:42px;font-weight:400">Get connected with us</h4>
  <div class="social"><i></i><i></i><i></i><i></i></div>
  <div class="col" style="left:883px;top:146px">Tech Support:</div>
  <div class="phone" style="top:172px">(800) 555-0147</div>
  <div class="col" style="left:883px;top:222px">General Support:</div>
  <div class="phone" style="top:248px">(100) 555-0182</div>
  <div class="copy">Copyright &copy; 2018 Quillmont Booking Engine. All Rights Reserved.</div>
  <span class="btn" style="left:883px;top:355px;width:242px;height:44px;font-size:15px">Start Your Free Trial</span>
</footer>

</body>
</html>
```